Say Something About Privacy!!!

We need a poster designed with the theme of "Privacy". With so many digital assistants (Vonu, Marvo, Plinker, etc) listening to our conversations and web cams watching our activities privacy is becoming more important than ever. The goal of the project is to design a poster that can be used as giveaway item at trade shows, etc. The poster should be engaging and thought provoking. The tone can be serious or lighthearted. You can use a photo, illustration, or just copy to get your point across. I've included a few examples of other posters I like.

Target Market(s)

General Public. Well educated. Tech enthusiasts. People with smartphones and/or smart speakers.

Industry/Entity Type

Cyber Security

Font styles to use
Sans Serif

Requirements
Must have
• Simple design. Strong colours.
Should not have
• While this is a serious subject, I don't want the message to be too threatening.

```html
<!DOCTYPE html>
<html lang="en">
<head>
<meta charset="utf-8">
<title>Privacy Poster – Take action, now</title>
<link rel="stylesheet" href="https://fonts.googleapis.com/css2?family=Raleway:wght@300;600;700;800&display=swap">
<style>
  :root {
    --backdrop: #e9e9e9;
    --poster-light: #c9c9c9;
    --poster-mid: #8a8a8a;
    --poster-dark: #464647;
    --dialog-bg: #eeeeee;
    --dialog-rule: #cfcfcf;
    --headline: #1d1d1f;
    --action-blue: #0a5cf5;
    --warning-yellow: #f7e62a;
    --warning-outline: #3a3a3c;
    --footer-light: #c6c6c6;
    --footer-strong: #e2e2e2;
  }
  * { margin: 0; padding: 0; box-sizing: border-box; }
  html, body {
    width: 1200px;
    height: 944px;
    overflow: hidden;
    background: var(--backdrop);
    font-family: "Raleway", sans-serif;
  }
  .canvas {
    position: relative;
    width: 1200px;
    height: 944px;
  }
  .poster {
    position: absolute;
    left: 266px;
    top: 0;
    width: 667px;
    height: 944px;
    background:
      radial-gradient(ellipse 62% 48% at 40% 32%, var(--poster-light) 0%, var(--poster-mid) 45%, rgba(70,70,71,0) 100%),
      var(--poster-dark);
    overflow: hidden;
  }
  .alert-dialog {
    position: absolute;
    left: 79px;
    top: 290px;
    width: 510px;
    height: 305px;
    background: var(--dialog-bg);
    border-radius: 18px;
    box-shadow: 10px 14px 16px rgba(0,0,0,0.45);
    overflow: hidden;
  }
  .alert-icon {
    position: absolute;
    left: 50%;
    top: 23px;
    width: 74px;
    height: 66px;
    transform: translateX(-50%);
    filter: drop-shadow(3px 4px 3px rgba(0,0,0,0.35));
  }
  .alert-title {
    position: absolute;
    left: 0;
    right: 0;
    top: 104px;
    text-align: center;
    font-weight: 700;
    font-size: 40px;
    line-height: 39px;
    letter-spacing: -0.3px;
    color: var(--headline);
  }
  .alert-actions {
    position: absolute;
    left: 0;
    right: 0;
    bottom: 0;
    height: 89px;
    display: flex;
    border-top: 1.5px solid var(--dialog-rule);
  }
  .alert-action {
    flex: 1;
    display: flex;
    align-items: center;
    justify-content: center;
    font-weight: 700;
    font-size: 26px;
    color: var(--action-blue);
  }
  .alert-action + .alert-action {
    border-left: 1.5px solid var(--dialog-rule);
  }
  .poster-footer {
    position: absolute;
    left: 0;
    right: 0;
    top: 828px;
    text-align: center;
    font-size: 19px;
    font-weight: 300;
    color: var(--footer-light);
  }
  .poster-footer .hashtag {
    font-weight: 700;
    color: var(--footer-strong);
  }
</style>
</head>
<body>
  <main class="canvas">
    <section class="poster">
      <div class="alert-dialog" role="alertdialog" aria-labelledby="alert-title">
        <svg class="alert-icon" viewBox="0 0 74 66" aria-hidden="true">
          <path d="M37 5 L70 60 Q71 63 68 63 L6 63 Q3 63 4 60 Z" fill="var(--warning-yellow)" stroke="var(--warning-outline)" stroke-width="4.5" stroke-linejoin="round"/>
          <rect x="34.2" y="20" width="5.6" height="27" rx="2" fill="var(--warning-outline)"/>
          <circle cx="37" cy="54" r="3.6" fill="var(--warning-outline)"/>
        </svg>
        <h1 class="alert-title" id="alert-title">Your data is under<br>the threat of leakage</h1>
        <div class="alert-actions">
          <span class="alert-action">Take action, now</span>
          <span class="alert-action">Regret later</span>
        </div>
      </div>
      <p class="poster-footer">It’s your choice. <span class="hashtag">#StayDataWise</span></p>
    </section>
  </main>
</body>
</html>
```